Etiketten-Design für Weinflasche
Helga hat mit sehr viel Mühe und Hingabe unsere Wünsche umgesetzt. Wir sind mit dem Endergebnis sehr zufrieden.
Zielgruppe
Wir sind ein Weingut-Startup und suchen ein frisches, hochwertiges Design für unsere Flaschenetiketten.
Aufgabenstellung
Wir benötigen ein Vorderetikett für unsere Weinflaschen mit folgenden Vorgaben:
- Etiketten sollen variabel nutzbar sein, für verschiedene Rebsorten bspw. in versch. Farben
- Auf dem Etikett zwingend: Logo (siehe Anlage), Rebsorte, Anbaugebiet (Nahe)
- Wiedererkennungswert
- nicht zu klassisch, nicht zu futuristisch (gutes Mittelmaß, wie beim Logo auch)
- ggf. Spiel mit (Hintergrund-)Farben für verschiedene Sorten, ggf. Hintergrundmuster (evtl. Höhenlinien des Talwiesers, Bad Kreuznach (unser Heimatberg))
- Anpassung an verschiedene Qualitätsstufen (Gutswein, Ortswein, Lagenwein), ggf. schwarzes Sonderetikett für absolutes Premiumsegment
- unsere Werte als Naturnah und familiengeführtes Weingut sollen transportiert werden
- Maß: 80x90mm (breitxhoch)
Insgesamt sind wir offen für verschiedene Vorschläge, auch wenn die Vorgaben oben teils sehr konkret sind. Bei guten Designs lassen wir uns gerne von unseren Vorstellungen abbringen ;)

```html
<!DOCTYPE html>
<html lang="de">
<head>
<meta charset="utf-8">
<title>Rebhain Weingut – Etiketten</title>
<link rel="stylesheet" href="https://fonts.googleapis.com/css2?family=Bebas+Neue&family=Poppins:wght@300;400;600&display=swap">
<style>
  :root {
    --stage: #000000;
    --paper: #ffffff;
    --paper-shade: #e4e4e4;
    --dornfelder: #56212f;
    --rose: #d59078;
    --riesling: #4f6953;
    --year-grey: #6f6f6f;
    --rule-grey: #b9b9b9;
    --region-grey: #a9a9a9;
  }
  * { box-sizing: border-box; margin: 0; padding: 0; }
  html, body { width: 1200px; height: 1199px; overflow: hidden; background: var(--stage); }
  .stage { position: relative; width: 1200px; height: 1199px; }

  .label {
    position: absolute;
    top: 365px;
    width: 340px;
    height: 457px;
    background: linear-gradient(90deg, var(--paper) 0%, var(--paper) 70%, var(--paper-shade) 100%);
    overflow: hidden;
  }
  .label--dornfelder { left: 28px;  --tone: var(--dornfelder); }
  .label--rose       { left: 430px; --tone: var(--rose); }
  .label--riesling   { left: 831px; --tone: var(--riesling); }

  .label__head {
    position: absolute; left: 0; top: 0;
    width: 310px; height: 142px;
    background: var(--tone);
    display: flex; align-items: center; justify-content: center;
    padding-right: 8px;
  }
  .brand {
    display: flex; align-items: center; gap: 8px;
    color: var(--paper);
    font-family: "Poppins", sans-serif;
    font-weight: 300;
    font-size: 34px;
    letter-spacing: 1px;
    margin-top: -6px;
  }
  .brand__dot { width: 14px; height: 14px; border-radius: 50%; background: var(--paper); }

  .label__band {
    position: absolute; left: 0; top: 155px;
    width: 340px; height: 200px;
    background: var(--tone);
  }
  .vineyard {
    position: absolute; right: 0; top: 78px;
    width: 160px; height: 72px;
    background: linear-gradient(160deg, rgba(255,255,255,0) 10%, rgba(255,255,255,0.16) 55%, rgba(255,255,255,0.05) 100%);
    clip-path: polygon(0 70%, 40% 20%, 100% 0, 100% 100%, 20% 100%);
  }
  .variety {
    position: absolute; left: 74px; top: 56px;
    font-family: "Bebas Neue", sans-serif;
    font-size: 32px; line-height: 33px;
    letter-spacing: 3.5px;
    color: var(--paper);
  }
  .region {
    position: absolute; left: 200px; top: 170px;
    font-family: "Bebas Neue", sans-serif;
    font-size: 19px; letter-spacing: 4px;
    color: var(--region-grey);
  }

  .label__foot { position: absolute; left: 0; top: 355px; width: 340px; height: 102px; }
  .quality {
    position: absolute; right: 116px; top: 24px;
    text-align: right;
    font-family: "Poppins", sans-serif;
    font-weight: 600; font-size: 8.5px; line-height: 12px;
    color: var(--tone);
  }
  .divider { position: absolute; left: 231px; top: 0; width: 1px; height: 102px; background: var(--rule-grey); }
  .vintage {
    position: absolute; left: 239px; top: 20px;
    font-family: "Poppins", sans-serif; font-weight: 400;
    font-size: 21px; color: var(--year-grey);
  }
</style>
</head>
<body>
<main class="stage">

  <article class="label label--dornfelder">
    <header class="label__head"><div class="brand"><span class="brand__dot"></span>Rebhain</div></header>
    <section class="label__band">
      <div class="vineyard" role="img" aria-label="Stilisierte Weinbergzeilen"></div>
      <h2 class="variety">Dornfelder<br>Feinherb</h2>
      <p class="region">Nahe</p>
    </section>
    <footer class="label__foot">
      <p class="quality">DEUTSCHER<br>QUALITÄTSWEIN</p>
      <span class="divider"></span>
      <p class="vintage">2024</p>
    </footer>
  </article>

  <article class="label label--rose">
    <header class="label__head"><div class="brand"><span class="brand__dot"></span>Rebhain</div></header>
    <section class="label__band">
      <div class="vineyard" role="img" aria-label="Stilisierte Weinbergzeilen"></div>
      <h2 class="variety">Dornfelder<br>Rosé</h2>
      <p class="region">Nahe</p>
    </section>
    <footer class="label__foot">
      <p class="quality">DEUTSCHER<br>QUALITÄTSWEIN</p>
      <span class="divider"></span>
      <p class="vintage">2024</p>
    </footer>
  </article>

  <article class="label label--riesling">
    <header class="label__head"><div class="brand"><span class="brand__dot"></span>Rebhain</div></header>
    <section class="label__band">
      <div class="vineyard" role="img" aria-label="Stilisierte Weinbergzeilen"></div>
      <h2 class="variety">Riesling<br>Feinherb</h2>
      <p class="region">Nahe</p>
    </section>
    <footer class="label__foot">
      <p class="quality">DEUTSCHER<br>QUALITÄTSWEIN</p>
      <span class="divider"></span>
      <p class="vintage">2024</p>
    </footer>
  </article>

</main>
</body>
</html>
```